"Velvet Petal Hour" Fashion Show Invitation design

We need an invitation design for our fashion show with the theme "Velvet Petal Hour"

the design will be the cover of the invitation, save the date cards, program etc

We are a philanthropic organization. Would like to incorporate florals, jewel tones or pastels etc... not sure if theres a way O or need) to incorporate fashion into that in an elegant way.

Text should read The Carrowfield Circle Presents "Velvet Petal Hour"
Updates

I'm looking for the design/image for the cover of our invitation- The only text needed is The Carrowfield Circle Presents Velvet Petal Hour I'm looking for feminine, elegant, florals etc...

Font styles to use
Serif
Decorative
Script

Colors
b768aa
e667a6
85cae6

Requirements
Must have
• jewel tones or pastels, flowers,
Nice to have
• fashion?

```html
<!DOCTYPE html>
<html lang="en">
<head>
<meta charset="utf-8">
<title>The Carrowfield Circle Presents Velvet Petal Hour</title>
<link rel="stylesheet" href="https://fonts.googleapis.com/css2?family=Playfair+Display:wght@700&family=Pinyon+Script&display=swap">
<style>
  :root {
    --sky: #8ccbe4;
    --rose: #e667a6;
    --orchid: #b768aa;
    --cornflower: #4f8fd6;
    --petal-white: #fbf4fa;
    --blush: #f3c1dc;
    --ink: #2c2427;
    --title-white: #ffffff;
  }
  * { margin: 0; padding: 0; box-sizing: border-box; }
  html, body {
    width: 1200px;
    height: 800px;
    overflow: hidden;
    background: var(--sky);
  }
  .invitation-cover {
    position: relative;
    width: 1200px;
    height: 800px;
    overflow: hidden;
    background: var(--sky);
  }
  .floral-field {
    position: absolute;
    inset: 0;
    width: 1200px;
    height: 800px;
  }
  .pink-frame {
    position: absolute;
    left: 31px;
    top: 22px;
    width: 1139px;
    height: 752px;
    border: 14px solid var(--rose);
    opacity: 0.72;
  }
  .grain {
    position: absolute;
    inset: 0;
    width: 1200px;
    height: 800px;
    pointer-events: none;
    mix-blend-mode: soft-light;
    opacity: 0.55;
  }
  .cover-text {
    position: absolute;
    inset: 0;
    text-align: center;
  }
  .host-name {
    position: absolute;
    top: 150px;
    left: 0;
    width: 100%;
    font-family: "Playfair Display", Georgia, serif;
    font-weight: 700;
    font-size: 72px;
    letter-spacing: 3px;
    color: var(--title-white);
    text-transform: uppercase;
    white-space: nowrap;
  }
  .presents {
    position: absolute;
    top: 255px;
    left: 0;
    width: 100%;
    font-family: "Playfair Display", Georgia, serif;
    font-weight: 700;
    font-size: 42px;
    letter-spacing: 1px;
    color: var(--title-white);
    text-transform: uppercase;
  }
  .show-title {
    position: absolute;
    top: 370px;
    left: 0;
    width: 100%;
    font-family: "Pinyon Script", cursive;
    font-weight: 400;
    font-size: 132px;
    line-height: 1;
    color: var(--ink);
    white-space: nowrap;
  }
</style>
</head>
<body>
<main class="invitation-cover">
  <svg class="floral-field" viewBox="0 0 1200 800" role="img" aria-label="Collage of pink and blue roses, pink peonies and white lilies scattered around the border over a faint lavender texture">
    <defs>
      <radialGradient id="rose-bloom" cx="50%" cy="50%" r="50%">
        <stop offset="0%" stop-color="#3f86d2"/>
        <stop offset="45%" stop-color="#b768aa"/>
        <stop offset="100%" stop-color="#e68ad0" stop-opacity="0.85"/>
      </radialGradient>
      <radialGradient id="peony-bloom" cx="50%" cy="50%" r="50%">
        <stop offset="0%" stop-color="#f0a6cf"/>
        <stop offset="60%" stop-color="#f6cde3"/>
        <stop offset="100%" stop-color="#f9e4f0" stop-opacity="0.9"/>
      </radialGradient>
      <radialGradient id="lily-bloom" cx="50%" cy="50%" r="50%">
        <stop offset="0%" stop-color="#d8f0ee"/>
        <stop offset="55%" stop-color="#fbf4fa"/>
        <stop offset="100%" stop-color="#ffffff" stop-opacity="0.9"/>
      </radialGradient>
    </defs>
    <ellipse class="center-texture" cx="620" cy="470" rx="360" ry="290" fill="#b49ad0" opacity="0.28"/>
    <circle cx="150" cy="180" r="230" fill="url(#rose-bloom)" opacity="0.9"/>
    <circle cx="1020" cy="150" r="150" fill="url(#rose-bloom)" opacity="0.92"/>
    <ellipse cx="880" cy="720" rx="230" ry="130" fill="url(#rose-bloom)" opacity="0.75"/>
    <ellipse cx="640" cy="60" rx="170" ry="85" fill="url(#peony-bloom)"/>
    <ellipse cx="280" cy="630" rx="170" ry="150" fill="url(#peony-bloom)"/>
    <ellipse cx="1160" cy="460" rx="90" ry="160" fill="url(#peony-bloom)"/>
    <ellipse cx="55" cy="790" rx="90" ry="60" fill="url(#peony-bloom)"/>
    <ellipse cx="360" cy="45" rx="110" ry="80" fill="url(#lily-bloom)"/>
    <ellipse cx="50" cy="590" rx="110" ry="140" fill="url(#lily-bloom)"/>
    <ellipse cx="520" cy="740" rx="150" ry="90" fill="url(#lily-bloom)"/>
    <ellipse cx="1120" cy="730" rx="110" ry="110" fill="url(#lily-bloom)"/>
    <ellipse cx="1165" cy="25" rx="60" ry="45" fill="url(#lily-bloom)"/>
  </svg>

  <div class="pink-frame"></div>

  <svg class="grain" viewBox="0 0 1200 800" aria-hidden="true">
    <filter id="paper-grain">
      <feTurbulence type="fractalNoise" baseFrequency="0.9" numOctaves="2" stitchTiles="stitch"/>
      <feColorMatrix type="saturate" values="0"/>
    </filter>
    <rect width="1200" height="800" filter="url(#paper-grain)"/>
  </svg>

  <header class="cover-text">
    <h1 class="host-name">The Carrowfield Circle</h1>
    <p class="presents">Presents</p>
    <h2 class="show-title">Velvet Petal Hour</h2>
  </header>
</main>
</body>
</html>
```